Ancient Art and Artifact information website

Hello Designers,
We are starting up a new website who talk abut and discusses an ancient arts artifacts. We would covering a wide range of countries ranging from Egypt, Greece, India, Syria, Rome, etc. My website name Brisk Loom
Designs that fits with ancient theme and some kind of uniqueness would be accepted.
Requirements:
1) A home page design
2) Sub page design
3) A suitable logo
Sections can be added are featured ancient arts/places with short description followed by a more button, latest news, and comment section.
Add contents if you found relevant for this category of website. Ability to share the information through social media is desired.
Must be a responsive design. I look forward to designs which are mind blowing.
2 page

```html
<!DOCTYPE html>
<html lang="en">
<head>
<meta charset="utf-8">
<title>Brisk Loom — Ancient Arts &amp; Artifacts</title>
<link href="https://fonts.googleapis.com/css2?family=Oswald:wght@300;400&family=Raleway:wght@400;500;600;700&display=swap" rel="stylesheet">
<style>
  :root {
    --gold: #b88a45;
    --gold-soft: #c9a063;
    --ink: #1c1a17;
    --body: #2b2926;
    --white: #ffffff;
    --paper: #f4f4f4;
    --dusk-top: #0d0f13;
    --dusk-mid: #3a2c1e;
    --stone: #5a4128;
    --earth: #3b2a16;
    --earth-deep: #2a1d0f;
    --sky-dark: #2e2212;
    --sky-warm: #6b4d26;
    --sand: #8a6634;
  }
  * { box-sizing: border-box; margin: 0; padding: 0; }
  html, body { width: 1200px; height: 2795px; overflow: hidden; }
  body { position: relative; background: var(--white); font-family: "Raleway", Arial, sans-serif; color: var(--body); }
  .abs { position: absolute; }

  /* Hero */
  .hero { left: 0; top: 0; width: 1200px; height: 609px; overflow: hidden; }
  .hero-photo { position: absolute; inset: 0;
    background: linear-gradient(180deg, var(--dusk-top) 0%, #1f2026 22%, var(--dusk-mid) 55%, var(--stone) 80%, #4a3522 100%); }
  .brand { left: 300px; top: 44px; width: 126px; text-align: center; color: var(--gold); font-size: 23px; font-weight: 500; line-height: 30px; }
  .nav { left: 473px; top: 51px; list-style: none; font-size: 11px; font-weight: 600; letter-spacing: 0.4px; }
  .nav li { position: absolute; top: 0; white-space: nowrap; color: var(--gold-soft); }
  .nav li.is-active { color: var(--white); }
  .slider-dots { left: 569px; top: 574px; display: flex; gap: 4px; }
  .slider-dots span { width: 8px; height: 8px; border-radius: 50%; background: var(--gold); }
  .slider-dots span.is-active { background: var(--white); }

  /* Welcome */
  .welcome { left: 0; top: 609px; width: 1200px; height: 414px; text-align: center; }
  .welcome-kicker { position: absolute; top: 36px; width: 100%; font-size: 24px; font-weight: 600; letter-spacing: 7px; color: var(--ink); }
  .welcome-title { position: absolute; top: 58px; width: 100%; font-family: "Oswald", "Arial Narrow", sans-serif; font-size: 50px; line-height: 56px; font-weight: 400; letter-spacing: 14px; color: var(--gold); }
  .welcome-copy { position: absolute; left: 250px; width: 720px; font-size: 13.5px; line-height: 17.5px; color: var(--body); letter-spacing: 0.7px; }

  /* Artifacts */
  .artifacts { left: 0; top: 1023px; width: 1200px; height: 552px; overflow: hidden; }
  .artifacts-bg { position: absolute; inset: 0;
    background: radial-gradient(ellipse at 55% 50%, #4d3a24 0%, var(--earth) 55%, var(--earth-deep) 100%); }
  .artifacts-title { position: absolute; top: 48px; width: 100%; text-align: center; font-size: 36px; font-weight: 700; letter-spacing: 2px; color: var(--gold); }
  .artifact-name { position: absolute; font-size: 18px; font-weight: 700; letter-spacing: 0.6px; color: var(--white); white-space: nowrap; }
  .artifact-note { position: absolute; font-size: 10.5px; line-height: 12px; color: #e6ddd0; width: 200px; }
  .is-right { text-align: right; }
  .artifact-photo { position: absolute; width: 100px; height: 100px; border-radius: 50%; border: 4px solid var(--white); }
  .photo-egypt { background: linear-gradient(160deg, #6aa3d6 0%, #c99a5a 55%, #8a5e2c 100%); }
  .photo-greece { background: linear-gradient(160deg, #3d6fa8 0%, #c27a45 55%, #7a4a2a 100%); }
  .photo-syria { background: linear-gradient(160deg, #5b93c9 0%, #c7b8a0 55%, #8e7c66 100%); }
  .photo-india { background: linear-gradient(160deg, #4f86c6 0%, #e9e6e2 55%, #b9b2a8 100%); }
  .photo-rome { background: linear-gradient(160deg, #6a9fd2 0%, #c48a55 55%, #8d5a32 100%); }
  .center-brand { left: 0; top: 1322px; width: 1140px; text-align: center; color: var(--gold); font-size: 21px; font-weight: 600; }

  /* Featured */
  .featured { left: 0; top: 1575px; width: 1200px; height: 702px; text-align: center; }
  .featured-kicker { position: absolute; top: 22px; width: 100%; font-size: 18px; font-weight: 500; letter-spacing: 5px; color: var(--ink); }
  .featured-title { position: absolute; top: 42px; width: 100%; font-family: "Oswald", "Arial Narrow", sans-serif; font-size: 46px; line-height: 54px; font-weight: 300; letter-spacing: 12px; color: var(--gold); }
  .place-tabs { position: absolute; top: 102px; width: 100%; display: flex; justify-content: center; gap: 18px; font-size: 11px; font-weight: 700; color: var(--ink); letter-spacing: 0.3px; list-style: none; }
  .place-tabs .sep { font-weight: 500; }
  .place-grid { position: absolute; left: 240px; top: 158px; display: grid; grid-template-columns: repeat(3, 231px); grid-auto-rows: 231px; gap: 5px; }
  .place-tile.taj { background: linear-gradient(180deg, #d9d4cd, #a49d93); }
  .place-tile.pyramid { background: linear-gradient(160deg, #4d8bd1 0%, #b88c5c 50%, #8a6440 100%); }
  .place-tile.sphinx { background: linear-gradient(160deg, #3f7bc4 0%, #a67f5a 55%, #6e5038 100%); }
  .place-tile.colosseum { background: linear-gradient(180deg, #e9a24c 0%, #c56c33 50%, #6a4a30 100%); }
  .place-tile.fountain { background: linear-gradient(180deg, #d6c7b0 0%, #b9a68a 60%, #4fb3c4 100%); }
  .place-tile.forum { background: linear-gradient(160deg, #c46a3f 0%, #b98658 50%, #7c6a3c 100%); }

  /* Closing band: pyramids under a cloudy sky */
  .closing { left: 0; top: 2277px; width: 1200px; height: 518px;
    background:
      radial-gradient(ellipse 420px 120px at 260px 90px, rgba(120,92,52,0.55), transparent 70%),
      radial-gradient(ellipse 500px 140px at 860px 150px, rgba(110,84,46,0.5), transparent 70%),
      radial-gradient(ellipse 380px 110px at 620px 40px, rgba(20,14,6,0.45), transparent 70%),
      radial-gradient(ellipse 300px 200px at 860px 470px, rgba(150,112,60,0.55), transparent 70%),
      radial-gradient(ellipse 260px 170px at 620px 480px, rgba(140,104,56,0.45), transparent 70%),
      linear-gradient(180deg, var(--sky-dark) 0%, #4a3519 35%, var(--sky-warm) 70%, var(--sand) 88%, #5a3f1c 100%); }
  .promo-top { left: 225px; top: 2476px; width: 233px; height: 138px; background: var(--gold); }
  .promo-bottom { left: 225px; top: 2614px; width: 233px; height: 128px; background: var(--paper); }
</style>
</head>
<body>

<header class="hero abs">
  <div class="hero-photo" role="img" aria-label="Dusk view of ancient Roman forum columns and a domed church"></div>
  <div class="brand abs">Brisk Loom</div>
  <ul class="nav abs">
    <li class="is-active" style="left:0">HOME</li>
    <li style="left:58px">ABOUT US</li>
    <li style="left:136px">BROWSE COUNTRY</li>
    <li style="left:267px">BLOGS</li>
    <li style="left:328px">NEWS</li>
    <li style="left:393px">FAQ</li>
    <li style="left:440px">CONTACT US</li>
  </ul>
  <div class="slider-dots abs"><span></span><span class="is-active"></span><span></span><span></span><span></span></div>
</header>

<section class="welcome abs">
  <h2 class="welcome-kicker">WELCOME TO</h2>
  <h1 class="welcome-title">BRISK LOOM</h1>
  <p class="welcome-copy" style="top:124px">Welcome to Lorem ipsum dolor sit amet, consectetur adipiscing elit. Fusce fringilla iaculis ante vel ornareat orci non elit elementum efficitur. Donec nibh lectus, bibendum aclibero eu, sagittislips faucibus velean volutpat euismod odiovel mollis Donec tincidunt pretium urna in vulputatet facilisis, mi eget sodales tincidunt, neque quam blandit diamis eros vitae neque. Maecenas finibus mi magna, sit amet ullamcorper mauris tempus a. Aenean posuere a neque sed accumsan. Nam facilisis dignissim ipsum in congue.</p>
  <p class="welcome-copy" style="top:261px">Donec tincidunt pretium urna in vulputate. Ut facilisis, mi eget sodales tincidunt, neque quam blandit diam, a aliquet felis eros vitae neque. Maecenas finibus mi magna, sit amet ullamcorper mauris tempus a. Aenean posuere a neque sed accumsan. Nam facilisis dignissim ipsum in congue.</p>
  <p class="welcome-copy" style="top:349px">Lorem ipsum dolor sit amet, consectetur adipiscing elit. Fusce fringilla iaculis ante vel ornare. Nunc at orci non elit elementum efficitur. Donec nibh lectus, bibendum ac libero eu, sagittis faucibus velit. Aenean volutpat euismod odio, vi eget sodales am, a aliquet felis eros vitaere a neque sed accumsan.</p>
</section>

<section class="artifacts abs">
  <div class="artifacts-bg" role="img" aria-label="Dimmed photo of ancient ruins with columns"></div>
  <h2 class="artifacts-title">AN ANCIENT ARTS ARTIFACTS</h2>

  <div class="artifact-name is-right" style="right:753px;top:148px">EGYPT ANCIENT ARTS ARTIFACTS</div>
  <p class="artifact-note is-right" style="right:753px;top:176px">Vestilum aclipsum diam sit amet quamveh icula elementum.</p>
  <div class="artifact-photo photo-egypt" role="img" aria-label="Great Sphinx of Giza" style="left:458px;top:138px"></div>

  <div class="artifact-photo photo-greece" role="img" aria-label="Ancient Greek amphitheatre" style="left:624px;top:171px"></div>
  <div class="artifact-name" style="left:734px;top:177px">GREECE ANCIENT ARTS ARTIFACTS</div>
  <p class="artifact-note" style="left:736px;top:205px">Vestilum aclipsum diam sit amet quamveh icula elementum.</p>

  <div class="artifact-name is-right" style="right:820px;top:317px">SYRIA ANCIENT ARTS ARTIFACTS</div>
  <p class="artifact-note is-right" style="right:820px;top:345px">Vestilum aclipsum diam sit amet quamveh icula elementum.</p>
  <div class="artifact-photo photo-syria" role="img" aria-label="Domed mosque in Syria" style="left:390px;top:291px"></div>

  <div class="artifact-photo photo-india" role="img" aria-label="Taj Mahal in India" style="left:641px;top:328px"></div>
  <div class="artifact-name" style="left:754px;top:348px">INDIA &nbsp;ANCIENT ARTS ARTIFACTS</div>
  <p class="artifact-note" style="left:756px;top:376px">Vestilum aclipsum diam sit amet quamveh icula elementum.</p>

  <div class="artifact-name is-right" style="right:706px;top:440px">ROME ANCIENT ARTS ARTIFACTS</div>
  <p class="artifact-note is-right" style="right:706px;top:468px">Vestilum aclipsum diam sit amet quamveh icula elementum.</p>
  <div class="artifact-photo photo-rome" role="img" aria-label="Roman forum ruins" style="left:509px;top:403px"></div>
</section>

<div class="center-brand abs">Brisk Loom</div>

<section class="featured abs">
  <h3 class="featured-kicker">ARTS PLACES</h3>
  <h2 class="featured-title">FEATURED ANCIENT</h2>
  <ul class="place-tabs">
    <li>EGYPT ANCIENT PLACES</li><li class="sep">|</li>
    <li>GREECE ANCIENT PLACES</li><li class="sep">|</li>
    <li>INDIA ANCIENT PLACES</li><li class="sep">|</li>
    <li>SYRIA ANCIENT PLACES</li><li class="sep">|</li>
    <li>ROME ANCIENT PLACES</li>
  </ul>
  <div class="place-grid">
    <div class="place-tile taj" role="img" aria-label="Carved marble facade of the Taj Mahal"></div>
    <div class="place-tile pyramid" role="img" aria-label="Stone pyramid under a blue sky"></div>
    <div class="place-tile sphinx" role="img" aria-label="Ram-headed sphinx statue in Egypt"></div>
    <div class="place-tile colosseum" role="img" aria-label="Colosseum in Rome at sunset"></div>
    <div class="place-tile fountain" role="img" aria-label="Baroque fountain with sculptures and turquoise water"></div>
    <div class="place-tile forum" role="img" aria-label="Columns of the Roman forum"></div>
  </div>
</section>

<section class="closing abs" role="img" aria-label="Pyramids in the desert under a cloudy golden sky"></section>
<div class="promo-top abs"></div>
<div class="promo-bottom abs"></div>

</body>
</html>
```